Business Card Design Project

Need a business card designed for a horse racing/gambling centered company.
Company name is PebbleLark.com.au
Company colours are similar to those in the logo.
Something clean and modern , designer given liberty to be creative.
Incorporate the logo is preferred.
Single or Double Sided fine
Must include :
Name
Mobile Number
Email Address
Reason: Apologies, I have been traveling unexpectedly with business and just need the extra two days to reply and give feedback before making a decision.

```html
<!DOCTYPE html>
<html lang="en">
<head>
<meta charset="utf-8">
<title>PebbleLark.com.au – Business Card</title>
<link rel="stylesheet" href="https://fonts.googleapis.com/css2?family=Open+Sans:wght@400;700&display=swap">
<style>
  :root {
    --backdrop: #c98b58;
    --card: #ffffff;
    --card-edge: #6b4a33;
    --ink-dark: #231f20;
    --ink-dark-2: #3a3637;
    --teal: #0e8f86;
    --teal-deep: #0b6e68;
    --text: #5a5a5a;
    --title-grey: #d4d4d4;
    --divider: #bdbdbd;
  }
  * { box-sizing: border-box; margin: 0; padding: 0; }
  html, body { width: 1200px; height: 440px; overflow: hidden; }
  body {
    background: var(--backdrop);
    font-family: "Open Sans", Arial, sans-serif;
    position: relative;
  }
  .card {
    position: absolute;
    top: 63px;
    width: 524px;
    height: 299px;
    background: var(--card);
    border: 1px solid var(--card-edge);
    border-radius: 18px;
    overflow: hidden;
  }
  .card--front { left: 57px; }
  .card--back { left: 618px; }

  .card__header { position: absolute; inset: 0 0 auto 0; width: 524px; height: 160px; }

  .holder { position: absolute; top: 14px; right: 40px; text-align: right; }
  .holder__name { color: #fff; font-weight: 700; font-size: 16px; line-height: 20px; }
  .holder__title { color: var(--title-grey); font-size: 14px; line-height: 20px; }

  .brand {
    position: absolute;
    display: flex;
    flex-direction: column;
    align-items: center;
    gap: 14px;
  }
  .card--front .brand { left: 58px; top: 118px; width: 184px; }
  .card--back .brand { left: 170px; top: 82px; width: 184px; }
  .brand__disc {
    width: 96px; height: 96px; border-radius: 50%;
    background: radial-gradient(circle at 45% 40%, var(--teal) 0%, var(--teal-deep) 100%);
  }
  .brand__name { color: var(--teal); font-weight: 700; font-size: 16px; white-space: nowrap; }

  .divider {
    position: absolute; left: 270px; top: 120px;
    width: 1px; height: 113px; background: var(--divider);
  }

  .contact {
    position: absolute; left: 287px; top: 123px;
    color: var(--text); font-size: 13px; line-height: 20px;
    list-style: none;
  }
  .contact__item { display: flex; align-items: center; gap: 5px; }
  .contact__icon { width: 10px; height: 10px; fill: var(--text); flex: none; }
  .contact__address { margin-top: 10px; }
</style>
</head>
<body>

  <section class="card card--front" aria-label="Business card front">
    <svg class="card__header" viewBox="0 0 524 160" aria-hidden="true">
      <defs>
        <linearGradient id="headerShade" x1="0" y1="0" x2="1" y2="0">
          <stop offset="0" stop-color="var(--ink-dark-2)"/>
          <stop offset="1" stop-color="var(--ink-dark)"/>
        </linearGradient>
      </defs>
      <path d="M0,0 H524 V122 C430,70 330,30 240,28 C140,26 60,40 0,58 Z" fill="url(#headerShade)"/>
      <path d="M0,60 C60,42 140,30 240,32 C330,34 430,74 524,126 V145 C430,88 330,48 230,45 C130,44 60,56 0,72 Z" fill="var(--teal)"/>
    </svg>

    <div class="holder">
      <p class="holder__name">Your Name</p>
      <p class="holder__title">Title</p>
    </div>

    <div class="brand">
      <div class="brand__disc" role="img" aria-label="Round company emblem area"></div>
      <p class="brand__name">PebbleLark.com.au</p>
    </div>

    <div class="divider"></div>

    <ul class="contact">
      <li class="contact__item">
        <svg class="contact__icon" viewBox="0 0 10 10" aria-hidden="true"><path d="M2,0.5 L4,2.5 L3,3.7 C3.6,5 5,6.4 6.3,7 L7.5,6 L9.5,8 L8.3,9.5 C4.5,9.2 0.8,5.5 0.5,1.7 Z"/></svg>
        <span>+61 400 555 012</span>
      </li>
      <li class="contact__item">
        <svg class="contact__icon" viewBox="0 0 10 10" aria-hidden="true"><path d="M2.5,0 H7.5 V10 H2.5 Z M3.3,1 V7.5 H6.7 V1 Z"/></svg>
        <span>+61 400 555 012</span>
      </li>
      <li class="contact__item">
        <svg class="contact__icon" viewBox="0 0 10 10" aria-hidden="true"><path d="M0.5,2 H9.5 V8 H0.5 Z M1,2.4 L5,5.4 L9,2.4"/></svg>
        <span>hello@pebblelark.com.au</span>
      </li>
      <li class="contact__address">Complex Name, Street Name<br>Area, City Name,000 000</li>
    </ul>
  </section>

  <section class="card card--back" aria-label="Business card back">
    <div class="brand">
      <div class="brand__disc" role="img" aria-label="Round company emblem area"></div>
      <p class="brand__name">PebbleLark.com.au</p>
    </div>
  </section>

</body>
</html>
```